Brackenridge Strength Studio Chronic Pain Flyer

Double sided DL flyer required to promote a strength training studio to sufferers of chronic pain. Flyer will be displayed in osteopathy, chiropractic and massage clinics. Flyer should be clean, professional and appeal to an older (40+) demographic.

Target Market(s)

Chronic pain sufferers. Age 40+

Industry/Entity Type

Health And Wellness

Colors

Designer to choose colors to be used in the design.

Requirements
Must have
• See attached files for text copy and logo. Image(s) of people strength training with a coach or personal trainer, as well as images depicting pain in common parts of the body (such as those pictured in the supplied mock up)
• website address: brackenridgestrengthstudio.example.com.au
• phone number : 0452 918 304
• Street address: 4/63 Juniper Hollow Rd, Brackenridge
Nice to have
• Images such as in the attached files.

```html
<!DOCTYPE html>
<html lang="en">
<head>
<meta charset="utf-8">
<title>Brackenridge Strength Studio – Chronic Pain Flyer</title>
<link rel="stylesheet" href="https://fonts.googleapis.com/css2?family=Montserrat:wght@400;600;700;800;900&family=Oswald:wght@700&family=Lato:wght@400;700&display=swap">
<style>
  :root {
    --ink: #141414;
    --red: #e31b23;
    --red-deep: #b5121a;
    --white: #ffffff;
    --paper-grey: #efefef;
    --line-grey: #8a8486;
    --text-grey: #3a3a3a;
    --stage: #d9d9d9;
  }
  * { box-sizing: border-box; margin: 0; padding: 0; }
  html, body { width: 1200px; height: 1200px; overflow: hidden; }
  body { background: var(--stage); position: relative; font-family: "Montserrat", sans-serif; }

  .flyer {
    position: absolute; top: 152px; width: 430px; height: 900px;
    background: var(--white); overflow: hidden;
    box-shadow: 0 6px 18px rgba(0,0,0,.28);
  }
  .flyer--front { left: 162px; }
  .flyer--back { left: 645px; }
  .flyer__art { position: absolute; inset: 0; width: 430px; height: 900px; display: block; }
  .flyer__layer { position: absolute; }

  .brand-name {
    text-align: center; font-family: "Montserrat", sans-serif; font-weight: 800;
    text-transform: uppercase; line-height: 1.05; letter-spacing: 1px;
  }
  .flyer--front .brand-name { left: 0; width: 430px; top: 56px; font-size: 24px; color: var(--white); }
  .flyer--back .brand-name { left: 220px; width: 170px; top: 136px; font-size: 17px; color: var(--ink); }

  .front-headline { left: 37px; top: 340px; width: 200px; }
  .front-headline__line {
    display: block; font-family: "Montserrat", sans-serif; font-weight: 900;
    color: var(--ink); line-height: 1; 
  }
  .front-headline__line--big { font-size: 38px; }
  .front-headline__line--mid { font-size: 32px; margin-top: 6px; margin-left: 4px; }
  .front-headline__tag {
    display: inline-block; margin-top: 6px; background: var(--red-deep); color: var(--white);
    font-family: "Oswald", sans-serif; font-weight: 700; font-size: 40px; line-height: 46px;
    padding: 0 10px; border-radius: 6px; letter-spacing: .5px;
  }

  .call-now {
    left: 0; width: 430px; top: 646px; text-align: center;
    font-weight: 400; font-size: 28px; letter-spacing: 3px; color: var(--ink);
  }
  .phone-pill {
    left: 45px; top: 693px; width: 350px; height: 62px; border-radius: 14px;
    background: var(--ink); color: var(--white); text-align: center;
    font-weight: 800; font-size: 38px; line-height: 62px;
    box-shadow: 0 6px 10px rgba(0,0,0,.2);
  }

  .contact-list { list-style: none; font-family: "Lato", sans-serif; font-size: 13px; }
  .contact-list li { display: flex; align-items: center; gap: 8px; height: 25px; }
  .contact-list svg { width: 15px; height: 15px; flex: none; }
  .flyer--front .contact-list { left: 101px; top: 782px; color: var(--text-grey); }
  .flyer--back .contact-list { left: 46px; top: 765px; color: var(--white); font-weight: 700; }

  .site-url {
    left: 0; width: 430px; text-align: center; color: var(--white);
    font-size: 9.5px; font-weight: 600; letter-spacing: 1.4px;
  }
  .flyer--front .site-url { top: 878px; }
  .flyer--back .site-url { top: 879px; }

  .back-headline { left: 0; width: 430px; top: 378px; text-align: center; color: var(--white); font-weight: 800; }
  .back-headline__small { display: block; font-size: 31px; letter-spacing: 1.5px; line-height: 38px; }
  .back-headline__big { display: block; font-size: 60px; letter-spacing: 2px; line-height: 64px; }

  .back-lead { left: 0; width: 430px; top: 521px; text-align: center; font-weight: 700; font-size: 18px; color: var(--ink); }
  .back-copy {
    left: 47px; width: 336px; font-size: 12.3px; line-height: 16.5px; color: var(--text-grey);
    text-align: justify;
  }
  .back-copy--one { top: 561px; }
  .back-copy--two { top: 644px; }
</style>
</head>
<body>

<!-- FRONT -->
<section class="flyer flyer--front">
  <svg class="flyer__art" viewBox="0 0 430 900" aria-hidden="false">
    <defs>
      <linearGradient id="backPhoto" x1="0" y1="0" x2="1" y2="1">
        <stop offset="0" stop-color="#cfcfcf"/>
        <stop offset=".55" stop-color="#a9a9a9"/>
        <stop offset="1" stop-color="#c98a8a"/>
      </linearGradient>
    </defs>
    <rect class="photo" x="180" y="180" width="250" height="400" fill="url(#backPhoto)" role="img" aria-label="Photo of a man's bare back with hands on shoulder and lower back, pain highlighted in red"/>
    <path d="M0,0H430V160C300,150 110,210 0,285Z" fill="var(--ink)"/>
    <path d="M0,285C110,210 300,150 430,160V185C300,176 110,230 0,305Z" fill="var(--red)"/>
    <path d="M0,480C80,560 250,590 430,555V900H0Z" fill="var(--paper-grey)"/>
    <path d="M0,480C80,560 250,590 430,555" fill="none" stroke="var(--ink)" stroke-width="7"/>
    <path d="M0,492C80,574 250,604 430,570" fill="none" stroke="var(--ink)" stroke-width="1.5"/>
    <path d="M0,880C150,850 300,850 430,868V900H0Z" fill="var(--red)"/>
  </svg>

  <div class="flyer__layer brand-name">Brackenridge<br>Strength Studio</div>

  <h1 class="flyer__layer front-headline">
    <span class="front-headline__line front-headline__line--big">HEALTH</span>
    <span class="front-headline__line front-headline__line--mid">THROUGH</span>
    <span class="front-headline__tag">STRENGTH</span>
  </h1>

  <p class="flyer__layer call-now">CALL NOW</p>
  <p class="flyer__layer phone-pill">0452 918 304</p>

  <ul class="flyer__layer contact-list">
    <li><svg viewBox="0 0 16 16"><path d="M8 1a5 5 0 0 0-5 5c0 4 5 9 5 9s5-5 5-9a5 5 0 0 0-5-5zm0 7a2 2 0 1 1 0-4 2 2 0 0 1 0 4z" fill="var(--red)"/></svg>4/63 Juniper Hollow Rd, Brackenridge</li>
    <li><svg viewBox="0 0 16 16"><path d="M1 6l7-4 7 4v8H1z" fill="var(--red)"/><path d="M1 6l7 5 7-5" fill="none" stroke="#fff" stroke-width="1.2"/></svg>info@brackenridgestrengthstudio.example.com.au</li>
  </ul>

  <p class="flyer__layer site-url">www.brackenridgestrengthstudio.example.com.au</p>
</section>

<!-- BACK -->
<section class="flyer flyer--back">
  <svg class="flyer__art" viewBox="0 0 430 900">
    <defs>
      <linearGradient id="kneePhoto" x1="0" y1="0" x2="1" y2="1">
        <stop offset="0" stop-color="#f1e3dc"/>
        <stop offset=".6" stop-color="#e9c9bd"/>
        <stop offset="1" stop-color="#f3d6d0"/>
      </linearGradient>
      <linearGradient id="redBand" x1="0" y1="0" x2="0" y2="1">
        <stop offset="0" stop-color="var(--red-deep)"/>
        <stop offset=".5" stop-color="var(--red)"/>
        <stop offset="1" stop-color="var(--red-deep)"/>
      </linearGradient>
    </defs>
    <rect x="0" y="200" width="430" height="176" fill="url(#redBand)"/>
    <path d="M0,226C110,318 300,308 430,284" fill="none" stroke="var(--white)" stroke-width="10"/>
    <path d="M0,215C110,307 300,297 430,273" fill="none" stroke="var(--line-grey)" stroke-width="12"/>
    <path d="M0,0H430V266C300,290 110,300 0,208Z" fill="var(--white)"/>
    <path d="M0,0H250V270C150,280 60,260 0,208Z" fill="url(#kneePhoto)" role="img" aria-label="Photo of hands holding a bare knee with the joint pain highlighted in red"/>
    <rect x="0" y="374" width="430" height="112" fill="var(--ink)"/>
    <path d="M0,766C150,748 300,750 430,770V900H0Z" fill="url(#redBand)"/>
    <path d="M0,880C150,858 300,856 430,868V900H0Z" fill="var(--ink)"/>
  </svg>

  <div class="flyer__layer brand-name">Brackenridge Strength Studio</div>

  <h2 class="flyer__layer back-headline">
    <span class="back-headline__small">HEALTH THROUGH</span>
    <span class="back-headline__big">STRENGTH</span>
  </h2>

  <p class="flyer__layer back-lead">You don’t have to live in pain.</p>
  <p class="flyer__layer back-copy back-copy--one">Strength training has been shown to improve many chronic pain conditions and is now being routinely recommended by medical and health professionals.</p>
  <p class="flyer__layer back-copy back-copy--two">Our private studio provides high quality strength training by expert strength coaches. We’ve helped countless people improve or eliminate chronic pain, contact us today and find out how we can help you.</p>

  <ul class="flyer__layer contact-list">
    <li><svg viewBox="0 0 16 16"><path d="M8 1a5 5 0 0 0-5 5c0 4 5 9 5 9s5-5 5-9a5 5 0 0 0-5-5zm0 7a2 2 0 1 1 0-4 2 2 0 0 1 0 4z" fill="none" stroke="#fff" stroke-width="1.4"/></svg>4/63 Juniper Hollow Rd, Brackenridge</li>
    <li><svg viewBox="0 0 16 16"><path d="M1 6l7-4 7 4v8H1z" fill="none" stroke="#fff" stroke-width="1.4"/><path d="M1 6l7 5 7-5" fill="none" stroke="#fff" stroke-width="1.2"/></svg>info@brackenridgestrengthstudio.example.com.au</li>
    <li><svg viewBox="0 0 16 16"><path d="M4 1l3 3-2 2c1 2 3 4 5 5l2-2 3 3-2 3C7 15 1 9 1 3z" fill="#fff"/></svg>0452 918 304</li>
  </ul>

  <p class="flyer__layer site-url">www.brackenridgestrengthstudio.example.com.au</p>
</section>

</body>
</html>
```